Bramblewick Dill Pickles needs your smart gourmet Design

Looking for a smart design for a dill pickle jar container. The text
Bramblewick Dill Pickles.
Simply Picklelicious.

A tasty reason to raid the refrigerator.

Target Market(s)

Foodies, farmers market types.

Font styles to use
Serif
Sans Serif

Colors

Designer to choose colors to be used in the design.

Requirements
Must have
• Attractive design to entice foodies to buy my Pickles. Not cluttered, easy to read.
Nice to have
• Pickles, garlic. Modern.
Should not have
• Clutter. No script text.

```html
<!DOCTYPE html>
<html lang="en">
<head>
<meta charset="utf-8">
<title>Bramblewick Dill Pickles – Label Variations</title>
<link rel="stylesheet" href="https://fonts.googleapis.com/css2?family=Anton&family=Oswald:wght@600&family=Fira+Sans+Condensed:wght@600&family=Fira+Sans:ital,wght@1,400&display=swap">
<style>
  :root {
    --paper: #ffffff;
    --label-orange: #cc3300;
    --label-red: #990000;
    --wave-line: #111111;
    --pickle-green: #4b6a1e;
    --pickle-dark: #2f4a12;
    --text-white: #ffffff;
  }
  * { margin: 0; padding: 0; box-sizing: border-box; }
  html, body {
    width: 1200px; height: 435px; overflow: hidden;
    background: var(--paper);
  }
  .sheet { position: relative; width: 1200px; height: 435px; }
  .label {
    position: absolute; top: 54px;
    width: 522px; height: 326px;
    overflow: hidden;
  }
  .label--boxed { left: 52px; }
  .label--italic { left: 626px; }
  .label__background { position: absolute; inset: 0; }
  .label__title {
    position: absolute; left: 0; width: 522px; top: 14px;
    text-align: center;
    font-family: "Anton", sans-serif;
    font-size: 80px; line-height: 82px;
    color: var(--text-white);
    text-transform: uppercase;
  }
  .label__product {
    position: absolute; left: 0; width: 522px; top: 198px;
    text-align: center;
    font-family: "Oswald", sans-serif; font-weight: 600;
    font-size: 34px; line-height: 40px;
    color: var(--text-white);
    text-transform: uppercase;
  }
  .tagline-box {
    position: absolute; left: 123px; top: 253px;
    width: 276px; height: 38px;
    background: var(--paper);
    display: flex; align-items: center; justify-content: center;
    font-family: "Fira Sans Condensed", sans-serif; font-weight: 600;
    font-size: 23px; color: var(--pickle-green);
  }
  .tagline-italic {
    position: absolute; left: 110px; width: 302px; top: 262px;
    text-align: center;
    font-family: "Fira Sans", sans-serif; font-style: italic; font-weight: 400;
    font-size: 23px; line-height: 28px;
    color: var(--text-white);
  }
  .label__subline {
    position: absolute; left: 0; width: 522px; top: 294px;
    text-align: center;
    font-family: "Fira Sans Condensed", sans-serif; font-weight: 600;
    font-size: 15px; line-height: 20px;
    color: var(--text-white);
  }
  .label--boxed .label__subline { width: 522px; left: 0; }
  .mascot {
    position: absolute; width: 72px; height: 88px;
    background: linear-gradient(180deg, var(--pickle-green), var(--pickle-dark));
    border-radius: 30px;
  }
  .label--boxed .mascot { left: 427px; top: 197px; }
  .label--italic .mascot { left: 423px; top: 199px; }
</style>
</head>
<body>
<main class="sheet">

  <section class="label label--boxed">
    <svg class="label__background" viewBox="0 0 522 326" width="522" height="326" aria-hidden="true">
      <rect width="522" height="326" fill="var(--label-orange)"/>
      <path d="M0,176 C40,190 90,192 140,208 C180,222 210,244 250,244 C320,244 360,220 400,222 C450,224 490,240 522,250 L522,326 L0,326 Z" fill="var(--label-red)"/>
      <path d="M0,176 C40,190 90,192 140,208 C180,222 210,244 250,244 C320,244 360,220 400,222 C450,224 490,240 522,250" fill="none" stroke="var(--wave-line)" stroke-width="2.5"/>
    </svg>
    <h1 class="label__title">Bramble<br>wick</h1>
    <p class="label__product">Dill Pickles</p>
    <p class="tagline-box">Simply Picklelicious!</p>
    <p class="label__subline">A tasty reason to raid the refrigerator.</p>
    <div class="mascot" role="img" aria-label="Illustration of two cartoon pickle characters"></div>
  </section>

  <section class="label label--italic">
    <svg class="label__background" viewBox="0 0 522 326" width="522" height="326" aria-hidden="true">
      <rect width="522" height="326" fill="var(--label-orange)"/>
      <path d="M0,176 C40,190 90,192 140,208 C180,222 210,244 250,244 C320,244 360,220 400,222 C450,224 490,240 522,250 L522,326 L0,326 Z" fill="var(--label-red)"/>
      <path d="M0,176 C40,190 90,192 140,208 C180,222 210,244 250,244 C320,244 360,220 400,222 C450,224 490,240 522,250" fill="none" stroke="var(--wave-line)" stroke-width="2.5"/>
    </svg>
    <h1 class="label__title">Bramble<br>wick</h1>
    <p class="label__product">Dill Pickles</p>
    <p class="tagline-italic">Simply Picklelicious!</p>
    <p class="label__subline">A tasty reason to raid the refrigerator.</p>
    <div class="mascot" role="img" aria-label="Illustration of two cartoon pickle characters"></div>
  </section>

</main>
</body>
</html>
```